Eye catching Stationary Design

Healthcare consultant firm looking for stationary design ( letterhead, envelope and business cards) That’s professional, classy and eye catching . The design should incorporate the logo and the colors of the logo in its design. You can see the logo on our website at www crestmore advisory. net.

```html
<!DOCTYPE html>
<html lang="en">
<head>
<meta charset="utf-8">
<title>Crestmore Advisory – Stationery</title>
<link rel="stylesheet" href="https://fonts.googleapis.com/css2?family=Cinzel:wght@400;600&family=PT+Sans:wght@400&family=Great+Vibes&display=swap">
<style>
:root{
  --stage:#bfc0c2;
  --brand:#0c5aa6;
  --accent:#2aa0da;
  --ink:#4b4b4d;
  --ink-dark:#2f2f31;
  --paper:#ffffff;
  --paper-shade:#eeeff1;
  --edge:#d4d5d8;
}
*{margin:0;padding:0;box-sizing:border-box}
html,body{width:1200px;height:708px;overflow:hidden}
body{background:var(--stage);position:relative;font-family:"PT Sans",sans-serif;color:var(--ink)}
.sheet{position:absolute;overflow:hidden}
.curve{position:absolute;left:0;top:0}
.icon{width:1em;height:1em;vertical-align:-0.12em;margin-right:0.45em;color:var(--accent)}
.brand-name{font-family:"Cinzel",serif;font-weight:600;color:var(--brand);white-space:nowrap}
.legal-name{font-family:"Cinzel",serif;font-weight:400;color:var(--ink-dark);white-space:nowrap}

/* Letterhead */
.letterhead{left:68px;top:58px;width:450px;height:582px;border:1px solid var(--edge);
  background:linear-gradient(160deg,var(--paper) 30%,var(--paper-shade) 100%)}
.letterhead .brand-name{position:absolute;left:0;right:0;top:16px;text-align:center;font-size:21px;letter-spacing:1px}
.letterhead .legal-name{position:absolute;left:0;right:0;top:48px;text-align:center;font-size:8px}
.letter{position:absolute;left:38px;top:132px;width:374px;font-size:8px;line-height:13.3px}
.letter .salutation{margin-bottom:10px}
.letter p{text-align:justify;margin-bottom:10px}
.letter .closing{font-size:10px;margin-top:14px}
.letter .signature{font-family:"Great Vibes",cursive;font-size:22px;color:var(--brand);margin-top:4px;line-height:1}
.letterhead .footer{position:absolute;left:0;right:0;text-align:center;font-size:6.5px}
.letterhead .footer.line-1{top:552px}
.letterhead .footer.line-2{top:564px}
.footer span{margin:0 6px}

/* Envelope */
.envelope-back{left:616px;top:76px;width:502px;height:225px;background:var(--paper)}
.envelope-back .brand-name{position:absolute;left:0;right:0;top:28px;text-align:center;font-size:22px;color:var(--paper);letter-spacing:1px}
.envelope-front{left:539px;top:194px;width:503px;height:225px;background:var(--paper);border:1px solid var(--edge)}
.envelope-front .brand-name{position:absolute;left:15px;width:140px;top:24px;text-align:center;font-size:15px}
.envelope-front .legal-name{position:absolute;left:15px;width:140px;top:50px;text-align:center;font-size:7.4px}
.envelope-front .address{position:absolute;left:13px;top:66px;font-size:6.5px}
.envelope-front .web{position:absolute;left:0;right:0;top:209px;text-align:center;font-size:7.5px;letter-spacing:2.6px;color:var(--ink-dark)}

/* Business cards */
.card{top:478px;width:185px;height:105px}
.card-front{left:603px;border:1px solid var(--edge);background:linear-gradient(110deg,var(--paper) 35%,var(--paper-shade) 100%)}
.card-front .brand-name{position:absolute;left:0;right:0;top:12px;text-align:center;font-size:11px}
.card-front .legal-name{position:absolute;left:0;right:0;top:32px;text-align:center;font-size:5.4px}
.card-front .person{position:absolute;left:0;right:0;top:48px;text-align:center;font-family:"Cinzel",serif;font-size:7px;color:var(--brand)}
.card-front .title{position:absolute;left:0;right:0;top:57px;text-align:center;font-family:"Cinzel",serif;font-size:4.6px;color:var(--ink-dark)}
.card-front .contact{position:absolute;left:0;right:0;text-align:center;font-size:4.4px}
.card-front .contact span{margin:0 3px}
.card-front .row-1{top:80px}
.card-front .row-2{top:87.5px}
.card-front .row-3{top:95.5px}
.card-back{left:799px;background:var(--brand)}
.card-back .pattern{position:absolute;inset:0;background:linear-gradient(135deg,#0e5fae,#0b549c)}
.card-back .brand-name{position:absolute;left:100px;width:60px;top:60px;text-align:center;font-size:9px;color:var(--paper)}
</style>
</head>
<body>

<svg width="0" height="0" style="position:absolute" aria-hidden="true">
  <symbol id="i-pin" viewBox="0 0 16 16"><circle cx="8" cy="8" r="6.5" fill="none" stroke="currentColor" stroke-width="1.4"/><path d="M8 3.8a2.6 2.6 0 0 0-2.6 2.6C5.4 8.6 8 11.8 8 11.8s2.6-3.2 2.6-5.4A2.6 2.6 0 0 0 8 3.8z" fill="currentColor"/></symbol>
  <symbol id="i-phone" viewBox="0 0 16 16"><path d="M4 1.5l2.2 3-1.3 1.6c.9 2 2.4 3.5 4.4 4.5l1.6-1.3 3 2.2-1.3 2.6C7.200 13.8 2.200 8.800 1.5 3z" fill="currentColor"/></symbol>
  <symbol id="i-mail" viewBox="0 0 16 16"><rect x="1" y="3" width="14" height="10" fill="currentColor"/><path d="M1.5 3.5L8 9l6.5-5.5" fill="none" stroke="#fff" stroke-width="1.2"/></symbol>
  <symbol id="i-globe" viewBox="0 0 16 16"><g fill="none" stroke="currentColor" stroke-width="1.2"><circle cx="8" cy="8" r="6.5"/><ellipse cx="8" cy="8" rx="2.8" ry="6.5"/><path d="M1.5 8h13M2.600 4.500h10.800M2.600 11.500h10.800"/></g></symbol>
</svg>

<!-- Letterhead -->
<section class="sheet letterhead">
  <div class="brand-name">Crestmore</div>
  <div class="legal-name">Crestmore Advisory LLC</div>
  <div class="letter">
    <div class="salutation">Dear Mr. Lorem,</div>
    <p>Lorem ipsum dolor sit amet, consectetuer adipiscing elit, sed diam nonummy nibh euismod tincidunt ut laoreet dolore magna aliquam erat volutpat. Ut wisi enim ad minim veniam, quis nostrud exerci tation ullamcorper suscipit lobortis nisl ut aliquip ex ea commodo consequat. Duis autem vel eum iriure dolor in hendiusto odio dignissim qui blandit praesent luptatum zzril delenit augue duis dolore te feugait nulla facilisi.</p>
    <p>Lorem ipsum dolor sit amet, consectetuer adipiscing elit, sed diam nonummy nibh euismod tincidunt ut laoreet dolore magna aliquam erat volutpat. Ut wisi enim ad minim veniam, quis nostrud exerci tation ullamcorper suscipit lobortis nisl ut aliquip ex ea commodo consequat. Duis autem vel eum iriure dolor in hendiusto odio dignissim qui blandit praesent luptatum zzril delenit augue duis dolore te feugait nulla facilisi.</p>
    <p>Lorem ipsum dolor sit amet, consectetuer adipiscing elit, sed diam nonummy nibh euismod tincidunt ut laoreet dolore magna aliquam erat volutpat. Ut wisi enim ad minim veniam, quis nostrud exerci tation ullamcorper suscipit lobortis nisl ut aliquip ex ea commodo consequat. Duis autem vel eum iriure dolor in hendiusto odio dignissim qui blandit praesent luptatum zzril delenit augue duis dolore te feugait nulla facilisi.</p>
    <div class="closing">Sincerely Your,</div>
    <div class="signature">Your Name</div>
  </div>
  <svg class="curve" width="450" height="582" aria-hidden="true"><path d="M0 571 Q225 503 450 571 Q225 515 0 571Z" fill="var(--brand)"/></svg>
  <div class="footer line-1"><svg class="icon"><use href="#i-pin"/></svg>1180 Harlow Street, Suite 12, Denver, CO 80204, USA</div>
  <div class="footer line-2">
    <span><svg class="icon"><use href="#i-phone"/></svg>(555) 214-0187</span>
    <span><svg class="icon"><use href="#i-mail"/></svg>info@crestmoreadvisory.net</span>
    <span><svg class="icon"><use href="#i-globe"/></svg>www.crestmoreadvisory.net</span>
  </div>
</section>

<!-- Envelope back with flap -->
<section class="sheet envelope-back">
  <svg class="curve" width="502" height="225" aria-hidden="true"><path d="M0 0H502C496 22 494 38 470 46L272 85Q251 90 230 85L32 46C8 38 6 22 0 0Z" fill="var(--brand)"/></svg>
  <div class="brand-name">Crestmore</div>
</section>

<!-- Envelope front -->
<section class="sheet envelope-front">
  <div class="brand-name">Crestmore</div>
  <div class="legal-name">Crestmore Advisory LLC</div>
  <div class="address"><svg class="icon"><use href="#i-pin"/></svg>1180 Harlow Street, Suite 12, Denver, CO 80204, USA</div>
  <svg class="curve" width="503" height="225" aria-hidden="true"><path d="M0 223 Q251 157 503 223 Q251 167 0 223Z" fill="var(--brand)"/></svg>
  <div class="web">www.crestmoreadvisory.net</div>
</section>

<!-- Business card front -->
<section class="sheet card card-front">
  <div class="brand-name">Crestmore</div>
  <div class="legal-name">Crestmore Advisory LLC</div>
  <div class="person">YOUR NAME</div>
  <div class="title">TITLE</div>
  <svg class="curve" width="185" height="105" aria-hidden="true"><path d="M0 80 Q92 54 185 80 Q92 60 0 80Z" fill="var(--brand)"/></svg>
  <div class="contact row-1"><svg class="icon"><use href="#i-phone"/></svg>(555) 214-0187</div>
  <div class="contact row-2"><span><svg class="icon"><use href="#i-mail"/></svg>info@crestmoreadvisory.net</span><span><svg class="icon"><use href="#i-globe"/></svg>www.crestmoreadvisory.net</span></div>
  <div class="contact row-3"><svg class="icon"><use href="#i-pin"/></svg>1180 Harlow Street, Suite 12, Denver, CO 80204, USA</div>
</section>

<!-- Business card back -->
<section class="sheet card card-back">
  <div class="pattern" role="img" aria-label="Repeating brand pattern in tonal blue"></div>
  <div class="brand-name">Crestmore</div>
</section>

</body>
</html>
```